Website Design for Forklift Training Company

DO NOT CONTACT PRIVATELY. ONLY SUBMISSIONS HERE WILL BE CONSIDERED

I need a design for a website that offers forklift training courses.

The company offers accredited, onsite forklift training that are customized for the needs of each individual company. The company offers a variety of courses to operate forklifts and other machinary.

About: "Pembrook Lift Academy Ltd delivers bespoke onsite forklift truck operator training throught the uk.
All our instructors have a wealth of knowledge and expertise to provide your company with all your forklift truck training requirements.
Pembrook Lift Academy Ltd is registered and accredited by qkmvd standards so you can be rest assured that all forklift training is carried out the very highest standard"

I need the following pages designed:
> a) Home Page: Include a header image, ways to contact, about snippet, overview of courses, accreditation that will be received after completing the courses. (See attachments for samples)
> b) About Page
> c) Contact Us Page
> d) Course Page Template: A page that will be used as template for the courses offered. It should contain;
1. Cover image for the course
2. A description of the course
3. A table indicating the various course options
4. Course Objectives
5. What the trainee will receive after doing the course (example: a certification)

Target Market(s)

Industrial Businesses

Number of Pages Required

4 page

Colors
0054AA
0677BA
7BADD7
CADEEF
E8F1F8
0094D4
00A9DD
6FCCEA
C7EBF8
E9F6FB

Requirements
Should not have
• - No Search bar

```html
<!DOCTYPE html>
<html lang="en">
<head>
<meta charset="utf-8">
<title>Forklift Training Website</title>
<link href="https://fonts.googleapis.com/css2?family=Ubuntu:wght@400;500;700&display=swap" rel="stylesheet">
<style>
:root{
  --navy:#0054AA;--blue:#0677BA;--sky:#7BADD7;--pale:#CADEEF;--mist:#E8F1F8;
  --azure:#0094D4;--cyan:#00A9DD;--aqua:#6FCCEA;--ice:#C7EBF8;--frost:#E9F6FB;
  --orange:#F7963C;--ink:#2b3440;--muted:#5c6673;--white:#fff;
}
*{margin:0;padding:0;box-sizing:border-box}
html,body{width:1200px;height:731px;overflow:hidden}
body{background:var(--navy);font-family:'Ubuntu',sans-serif;color:var(--ink);position:relative}
.page{position:absolute;top:0;width:560px;height:731px;background:var(--white);overflow:hidden}
.page-home{left:27px}
.page-courses{left:613px}
.abs{position:absolute}
/* home */
.site-header{left:0;top:0;width:560px;height:39px;background:var(--azure)}
.nav{right:24px;top:15px;display:flex;gap:13px;font-size:7px;color:var(--white)}
.about-band{left:0;top:39px;width:560px;height:300px}
.about-title{left:61px;top:64px;font-size:18px;color:var(--blue);font-weight:400}
.about-lead{left:61px;top:95px;width:210px;font-size:11.5px;line-height:16.5px;color:var(--blue)}
.about-body{left:61px;top:156px;width:220px;font-size:5.6px;line-height:11.7px;color:var(--ink)}
.about-photo{left:322px;top:70px;width:177px;height:177px;border-radius:2px;background:radial-gradient(circle at 50% 50%,#6f8c7a 0,#3e4c48 22%,#1f2523 55%,#141817 100%)}
.section-title{left:61px;top:305px;font-size:18px;color:var(--blue)}
.course-card{top:339px;width:140px;background:var(--white);box-shadow:0 2px 8px rgba(0,60,120,.15)}
.course-card .band{height:25px}
.course-card h3{font-weight:400;font-size:11.5px;line-height:16.5px;text-align:center;color:var(--ink);padding:21px 10px 0}
.course-card hr{border:0;border-top:1px solid #e4e8ec;margin:12px 18px 18px}
.btn{display:block;background:var(--orange);color:var(--white);font-size:7px;text-align:center;text-transform:uppercase;letter-spacing:.2px}
.course-card .btn{width:84px;height:19px;line-height:19px;margin:0 auto 19px}
.course-card ul{list-style:none;padding:0 16px 10px 16px}
.course-card li{font-size:5.5px;line-height:12.5px;color:var(--blue);position:relative;padding-left:6px}
.course-card li::before{content:"";position:absolute;left:0;top:5.5px;width:1.6px;height:1.6px;border-radius:50%;background:var(--ink)}
/* courses page */
.hero{left:0;top:0;width:560px;height:145px;background:linear-gradient(90deg,#4a3d3d 0,#7a6e70 30%,#a49ea2 55%,#8c7a7c 78%,#5d4b4d 100%)}
.hero-shade{left:0;top:0;width:560px;height:145px;background:linear-gradient(90deg,rgba(20,20,25,.55),rgba(20,20,25,.1))}
.hero-title{left:60px;top:30px;font-size:12px;font-weight:500;color:var(--white)}
.hero-text{left:60px;top:50px;width:220px;font-size:5.5px;line-height:11.5px;color:var(--white)}
.hero-btn{left:60px;top:88px;width:84px;height:18px;line-height:18px}
.dots{display:flex;gap:6px}
.dots span{width:5px;height:5px;border-radius:50%;background:#c9ccd0}
.dots span.on{background:#111}
.hero-dots{left:258px;top:133px}
.hero-dots span{background:rgba(255,255,255,.45)}
.hero-dots span.on{background:#111}
.row-title{left:60px;font-size:18px;color:var(--ink)}
.card-row{left:60px;display:grid;grid-template-columns:repeat(4,102px);gap:10px}
.tcard{background:var(--white);height:214px;position:relative;box-shadow:0 2px 7px rgba(0,40,90,.13)}
.tcard .thumb{height:78px;background:linear-gradient(180deg,#b9c0c8 0,#9aa3ad 45%,#c44a4a 78%,#a7aeb6 100%);position:relative}
.tag{position:absolute;left:3px;top:7px;background:#13234a;color:var(--white);font-size:4.6px;padding:1px 3px}
.tcard .body{padding:9px 7px 0}
.tcard h4{font-size:5.6px;font-weight:500;margin-bottom:4px}
.tcard p{font-size:4.8px;line-height:8px;color:var(--muted)}
.tcard .obj{font-size:4.8px;font-weight:500;margin:7px 0 3px;color:var(--ink)}
.tcard ol{list-style:none;font-size:4.8px;line-height:8.2px;color:var(--muted);padding-left:2px}
.tcard .btn{position:absolute;left:9px;bottom:8px;width:84px;height:19px;line-height:19px}
.arrow{width:12px;height:18px}
</style>
</head>
<body>

<section class="page page-home">
  <svg class="abs about-band" viewBox="0 0 560 300" aria-hidden="true"><path d="M0 0H560V80C470 210 250 260 0 145Z" fill="var(--mist)"/></svg>
  <header class="abs site-header"></header>
  <nav class="abs nav"><span>Home</span><span>About</span><span>Courses</span><span>Contact Us</span></nav>

  <h1 class="abs about-title">About Snippet</h1>
  <p class="abs about-lead">Pembrook Lift Academy Ltd delivers bespoke onsite forklift truck operator training throught the uk.</p>
  <p class="abs about-body">All our instructors have a wealth of knowledge and expertise to provide your company with all your forklift truck training requirements. Pembrook Lift Academy Ltd is registered and accredited by qkmvd standards so you can be rest assured that all forklift training is carried out the very highest standard.</p>
  <div class="abs about-photo" role="img" aria-label="Photo of a forklift operator loading pallets inside a lorry trailer"></div>

  <h2 class="abs section-title">Overview of Courses</h2>

  <article class="abs course-card" style="left:61px">
    <div class="band" style="background:var(--aqua)"></div>
    <h3>Mewp Training Courses</h3><hr>
    <a class="btn">Read More</a>
    <ul><li>Cherry Picker Training Course</li><li>Scissor Lift Training Course</li><li>Harness and Lanyard Training Course</li></ul>
  </article>
  <article class="abs course-card" style="left:210px">
    <div class="band" style="background:var(--cyan)"></div>
    <h3>Forklift Training Courses</h3><hr>
    <a class="btn">Read More</a>
    <ul><li>Varro Truck Training Course</li><li>Multiway Training Course</li><li>Counterbalance Training Course</li><li>Pivora Truck Training Course</li><li>Loadarm Crane Training Course</li><li>Llop Training Course</li><li>Mountrak Truck Training Course</li><li>Order Picker Truck Training Course</li><li>Pedestrian Training Course</li><li>Pivot Steer Training Course</li><li>Reach Training Course</li><li>Rough Terrain Training Course</li></ul>
  </article>
  <article class="abs course-card" style="left:359px">
    <div class="band" style="background:var(--aqua)"></div>
    <h3>Other Training Courses</h3><hr>
    <a class="btn">Read More</a>
    <ul><li>Terrik Truck Training Course</li><li>Front Loading Shovel Training Course</li><li>Overhead Pendant Crane Training Course</li><li>Swing Colum Jib Crane Training Course</li><li>Slinging and Signalling Training Course</li><li>Vehicle Banksman Training Course</li></ul>
  </article>
</section>

<section class="page page-courses">
  <svg class="abs" style="left:0;top:140px" width="560" height="120" viewBox="0 0 560 120" aria-hidden="true"><path d="M0 0H560V5C400 30 230 75 0 55Z" fill="var(--mist)"/></svg>
  <div class="abs hero" role="img" aria-label="Photo of a warehouse aisle with racking and red forklift trucks"></div>
  <div class="abs hero-shade"></div>
  <h2 class="abs hero-title">Varro Truck Training Course</h2>
  <p class="abs hero-text">Qui necessitatibus fuga et odio. Animi aut voluptates dolorem. Blanditiis qui sit voluptatum officia enim. Ipsum ut et sint accusamus libero. Deserunt enim.</p>
  <a class="abs btn hero-btn">Read More</a>
  <div class="abs dots hero-dots"><span></span><span></span><span></span><span class="on"></span></div>

  <h2 class="abs row-title" style="top:189px">Forklift Training Course</h2>
  <div class="abs card-row" style="top:228px">
    <article class="tcard"><div class="thumb" role="img" aria-label="Photo of forklift trucks in a warehouse"><span class="tag">Certificate</span></div><div class="body"><h4>Varro Truck Training Course</h4><p>Qui necessitatibus fuga et odio animi aut voluptates dolorem.</p><div class="obj">Course objective:</div><ol><li>1. Necessitatibus</li><li>2. ...</li><li>3. ...</li><li>4. ...</li></ol></div><a class="btn">Read More</a></article>
    <article class="tcard"><div class="thumb" role="img" aria-label="Photo of forklift trucks in a warehouse"><span class="tag">Certificate</span></div><div class="body"><h4>Varro Truck Training Course</h4><p>Qui necessitatibus fuga et odio animi aut voluptates dolorem.</p><div class="obj">Course objective:</div><ol><li>1. Necessitatibus</li><li>2. ...</li><li>3. ...</li><li>4. ...</li></ol></div><a class="btn">Read More</a></article>
    <article class="tcard"><div class="thumb" role="img" aria-label="Photo of forklift trucks in a warehouse"><span class="tag">Certificate</span></div><div class="body"><h4>Varro Truck Training Course</h4><p>Qui necessitatibus fuga et odio animi aut voluptates dolorem.</p><div class="obj">Course objective:</div><ol><li>1. Necessitatibus</li><li>2. ...</li><li>3. ...</li><li>4. ...</li></ol></div><a class="btn">Read More</a></article>
    <article class="tcard"><div class="thumb" role="img" aria-label="Photo of forklift trucks in a warehouse"><span class="tag">Certificate</span></div><div class="body"><h4>Varro Truck Training Course</h4><p>Qui necessitatibus fuga et odio animi aut voluptates dolorem.</p><div class="obj">Course objective:</div><ol><li>1. Necessitatibus</li><li>2. ...</li><li>3. ...</li><li>4. ...</li></ol></div><a class="btn">Read More</a></article>
  </div>
  <svg class="abs arrow" style="left:522px;top:326px" viewBox="0 0 12 18" aria-hidden="true"><path d="M2 2L10 9L2 16" fill="none" stroke="var(--ink)" stroke-width="2.2"/></svg>
  <div class="abs dots" style="left:263px;top:455px"><span></span><span></span><span></span><span class="on"></span></div>

  <h2 class="abs row-title" style="top:486px">Mewp Training Course</h2>
  <div class="abs card-row" style="top:525px">
    <article class="tcard"><div class="thumb" role="img" aria-label="Photo of forklift trucks in a warehouse"><span class="tag">Certificate</span></div><div class="body"><h4>Varro Truck Training Course</h4><p>Qui necessitatibus fuga et odio animi aut voluptates dolorem.</p><div class="obj">Course objective:</div><ol><li>1. Necessitatibus</li><li>2. ...</li><li>3. ...</li><li>4. ...</li></ol></div><a class="btn">Read More</a></article>
    <article class="tcard"><div class="thumb" role="img" aria-label="Photo of forklift trucks in a warehouse"><span class="tag">Certificate</span></div><div class="body"><h4>Varro Truck Training Course</h4><p>Qui necessitatibus fuga et odio animi aut voluptates dolorem.</p><div class="obj">Course objective:</div><ol><li>1. Necessitatibus</li><li>2. ...</li><li>3. ...</li><li>4. ...</li></ol></div><a class="btn">Read More</a></article>
    <article class="tcard"><div class="thumb" role="img" aria-label="Photo of forklift trucks in a warehouse"><span class="tag">Certificate</span></div><div class="body"><h4>Varro Truck Training Course</h4><p>Qui necessitatibus fuga et odio animi aut voluptates dolorem.</p><div class="obj">Course objective:</div><ol><li>1. Necessitatibus</li><li>2. ...</li><li>3. ...</li><li>4. ...</li></ol></div><a class="btn">Read More</a></article>
    <article class="tcard"><div class="thumb" role="img" aria-label="Photo of forklift trucks in a warehouse"><span class="tag">Certificate</span></div><div class="body"><h4>Varro Truck Training Course</h4><p>Qui necessitatibus fuga et odio animi aut voluptates dolorem.</p><div class="obj">Course objective:</div><ol><li>1. Necessitatibus</li><li>2. ...</li><li>3. ...</li><li>4. ...</li></ol></div><a class="btn">Read More</a></article>
  </div>
  <svg class="abs arrow" style="left:522px;top:624px" viewBox="0 0 12 18" aria-hidden="true"><path d="M2 2L10 9L2 16" fill="none" stroke="var(--ink)" stroke-width="2.2"/></svg>
</section>

</body>
</html>
```